Zaberu - Wordpress website for hot new GIF booth

We need a responsive website for a new brand we're launching. Scrolling parallax style. We are a event photo company offering the hottest new GIF booths. We want our site to be sleek, sexy, moving.

Here's some sites we like:
https://www.tundrix.com/us/
http://kelvasnap.com/
http://lark9.drumvelisaphone.com/

Target Market(s)

advertising agencies, marketing agencies, major brands, corporate planners, millenials

Industry/Entity Type

Events

Number of Pages Required

1 page

Font styles to use
Sans Serif

Colors
33b8a4
86cfc6
ffffff

Requirements
Must have
• I want it very much like this: https://www.tundrix.com/us/
• lots of imagery, movement
• Here's some competitors:
• http://www.quellarix.com/
• http://runbrightwick.com/
• http://www.dqrstudio.com/gif-photo-booth-rental/
• http://kelvasnap.com/
Nice to have
• slider at top with different booth designs
Should not have
• no bulky tabs at top

```html
<!DOCTYPE html>
<html lang="en">
<head>
<meta charset="utf-8">
<title>Zaberu — GIF Photo Booth</title>
<link href="https://fonts.googleapis.com/css2?family=Raleway:wght@300;400;500;600;700&family=Lato:wght@400;700&display=swap" rel="stylesheet">
<style>
:root{
  --teal:#33b8a4;
  --teal-soft:#86cfc6;
  --white:#ffffff;
  --ink:#2a2a2a;
  --text:#4a4a4a;
  --dark:#2e3030;
  --darker:#1f2020;
  --footer:#2b2b2b;
  --rule:#e4e4e4;
  --hero-pink:#d9628f;
  --hero-grey:#8e8a93;
  --hero-deep:#4a3a44;
}
*{box-sizing:border-box;margin:0;padding:0}
html,body{width:1200px;height:2917px;overflow:hidden}
body{position:relative;background:var(--white);font-family:'Raleway',sans-serif;color:var(--text)}
.abs{position:absolute}
.teal{color:var(--teal)}

/* header */
.site-header{position:absolute;left:0;top:0;width:1200px;height:86px;background:var(--white);border-bottom:2px solid var(--teal-soft)}
.brand{position:absolute;left:100px;top:22px;display:flex;align-items:center;gap:10px;font-family:'Raleway',sans-serif;font-weight:500;font-size:34px;letter-spacing:2px;color:var(--ink)}
.brand-square{width:38px;height:38px;background:var(--ink)}
.main-nav{position:absolute;right:100px;top:32px;display:flex;font-family:'Lato',sans-serif;font-size:14px;color:var(--ink)}
.main-nav a{color:inherit;text-decoration:none;padding:0 20px;border-left:1px solid #ddd;line-height:16px}
.main-nav a:first-child{border-left:none}
.main-nav a.active{color:var(--teal);position:relative}
.main-nav a.active::after{content:"";position:absolute;left:20px;right:20px;top:34px;height:2px;background:var(--teal)}

/* hero */
.hero{position:absolute;left:0;top:86px;width:1200px;height:540px;
  background:linear-gradient(90deg,var(--hero-pink) 0%,var(--hero-grey) 30%,var(--hero-deep) 50%,var(--hero-grey) 70%,var(--hero-pink) 100%)}
.hero-caption{position:absolute;left:657px;top:313px;width:452px;height:111px;background:rgba(40,40,40,.55);display:flex;align-items:center;gap:22px}
.hero-caption .mark{flex:none;width:100px;height:111px;background:#1c1c1c}
.hero-caption h1{font-weight:700;font-size:25px;color:var(--white);margin-bottom:6px}
.hero-caption p{font-size:14px;line-height:20px;color:var(--white);width:320px}

/* shared */
.section-title{font-weight:400;font-size:28px;color:var(--ink);line-height:38px}
.body-copy{font-size:13.5px;line-height:27px;color:var(--text)}
.btn{position:absolute;display:flex;align-items:center;height:37px;width:126px;background:var(--teal);color:var(--white);font-size:13px;text-decoration:none}
.btn::before{content:"";width:32px;height:37px;background:var(--ink);margin-right:14px}

/* gif section */
.tablet{position:absolute;left:101px;top:677px;width:444px;height:296px;border-radius:18px;background:#111;padding:18px}
.tablet .screen{width:100%;height:100%;background:linear-gradient(135deg,#6b5a52,#a99384 50%,#4d4440)}

/* dark section */
.future{position:absolute;left:0;top:1031px;width:1200px;height:472px;background:linear-gradient(120deg,#3a3d3c,#252727 55%,#2f3a38)}
.future h2{position:absolute;left:99px;top:56px;font-weight:400;font-size:29px;color:var(--white)}
.future .body-copy{position:absolute;left:99px;top:100px;width:730px;color:#d8d8d8}
.features{position:absolute;top:262px;list-style:none;font-size:13.5px;color:#e5e5e5}
.features li{display:flex;align-items:center;gap:12px;height:35px}
.features svg{width:14px;height:14px}
.feature-divider{position:absolute;left:327px;top:256px;width:1px;height:120px;background:#666}
.kiosk{position:absolute;left:856px;top:992px;width:155px;height:398px;border-radius:24px 24px 6px 6px;background:linear-gradient(180deg,#222 0 14%,#f1f1f1 14% 80%,#2a2a2a 80%)}

/* social section */
.phones{position:absolute;left:97px;top:1566px;width:273px;height:259px;display:flex;gap:21px}
.phones div{flex:1;border-radius:20px;background:linear-gradient(180deg,#e9ecef,#c9ced3);border:2px solid #d5d8db}

/* galleries */
.galleries{position:absolute;left:0;top:1873px;width:1200px;height:280px;background:linear-gradient(180deg,#1d1a22,#2a2430 60%,#1a171c)}
.galleries h2{position:absolute;left:0;width:1200px;top:48px;text-align:center;font-weight:400;font-size:28px;color:var(--white)}
.thumb{position:absolute;top:103px;width:189px;height:127px}
.thumb-caption{position:absolute;left:0;bottom:0;width:189px;height:32px;background:var(--teal);color:var(--white);font-size:13px;font-weight:600;display:flex;align-items:center;padding-left:10px;gap:8px}
.arrow{position:absolute;top:152px;width:26px;height:26px;border:1px solid #aaa;border-radius:50%}

/* blog */
.blog-title{position:absolute;left:0;width:1200px;top:2190px;text-align:center}
.card{position:absolute;top:2249px;width:316px}
.card .photo{height:149px;position:relative}
.date{position:absolute;left:0;top:8px;width:56px;height:70px;background:var(--teal);color:var(--white);text-align:center;font-weight:700;line-height:1}
.date b{display:block;font-size:22px;padding-top:6px}
.date span{display:block;font-size:11px;margin-top:2px}
.card h3{font-family:'Lato',sans-serif;font-weight:400;font-size:14px;color:var(--ink);margin-top:24px}
.meta{display:flex;gap:8px;align-items:center;font-size:11.5px;color:var(--ink);margin-top:12px}
.meta i{display:inline-block;width:10px;height:10px;background:var(--teal);border-radius:2px}
.card p{font-size:11px;line-height:17px;color:var(--ink);margin-top:12px}

/* footer */
.site-footer{position:absolute;left:0;top:2548px;width:1200px;height:315px;background:var(--footer)}
.quote-box{position:absolute;left:99px;top:2538px;width:247px;height:296px;background:var(--darker);padding:0 14px}
.site-footer h4,.quote-box h4{font-weight:700;font-size:16px;color:var(--white)}
.quote-box h4{margin-top:32px;margin-bottom:20px}
.field{height:33px;background:var(--white);margin-bottom:9px;font-size:11px;color:#999;padding:10px 12px}
.submit{width:102px;height:34px;background:#e9e9e9;color:var(--ink);font-size:12px;text-align:center;line-height:34px;margin-top:12px}
.fcol{position:absolute;top:45px}
.fcol h4::after{content:"";display:block;width:26px;height:2px;background:var(--white);margin-top:10px}
.links{list-style:none;margin-top:18px;font-size:12px;color:#ccc;line-height:26px}
.links li::before{content:"»";margin-right:10px}
.contact-row{display:flex;gap:16px;font-size:12px;color:#ccc;line-height:19px;margin-top:18px}
.contact-row svg{flex:none;width:16px;height:16px;margin-top:2px}
.socials{display:flex;gap:8px;margin-top:22px}
.socials span{width:24px;height:24px;background:var(--teal)}
.footer-brand{position:absolute;left:932px;top:2746px;font-weight:400;font-size:30px;letter-spacing:2px;color:var(--white)}
.copyright{position:absolute;left:0;top:2863px;width:1200px;height:54px;background:#0e0e0e;color:#ddd;font-size:12px;text-align:center;line-height:54px}
</style>
</head>
<body>

<header class="site-header">
  <div class="brand"><span class="brand-square"></span>Zaberu</div>
  <nav class="main-nav">
    <a class="active">Home</a><a>About Us</a><a>GIF Photo Booth</a><a>Event Galleries</a><a>Blog</a><a>Contact Us</a>
  </nav>
</header>

<section class="hero">
  <div class="abs" style="left:0;top:0;width:1200px;height:540px" role="img" aria-label="Hero photo: two guests posing at a GIF photo booth in front of a pink and grey backdrop"></div>
  <div class="hero-caption">
    <div class="mark"></div>
    <div>
      <h1>Welcome To Zaberu</h1>
      <p>Lorem Ipsum is simply du and typesetting industry dummy text ever since the</p>
    </div>
  </div>
</section>

<div class="tablet"><div class="screen" role="img" aria-label="Tablet showing a grid of booth photos with a video play button"></div></div>
<h2 class="section-title abs" style="left:583px;top:673px">GIF Photo <span class="teal">Booth</span></h2>
<p class="body-copy abs" style="left:585px;top:722px;width:520px">Lorem Ipsum is simply dummy text of the printing and typesetting industry. Lorem Ipsum has been the industry's standard dummy text ever since the 1500s, when an unknown printer took a galley of type and scrambled it to make a type specimen book. It has survived not only five centuries, but also the leap into electronic typesettin gublishing software like Quirel PageSetter including versions of Lorem Ipsum.</p>
<a class="btn" style="left:585px;top:912px">Read More</a>

<section class="future">
  <h2>Zaberu: The GIF Photo Booth Of The Future</h2>
  <p class="body-copy">Lorem Ipsum is simply dummy text of the printing and typesetting industry. Lorem Ipsum has been the industry's standard dummy text ever since the 1500s, when an unknown printer took a galley of type and scrambled it to make a type specimen book. It has survived not only five centuries,when an unknown printer took a galley of type and scrambled it to make a type specimen book. It has survived not only five centurieswhen an unknown printer took a galley of type and scrambled it to make a type specimen book.</p>
  <ul class="features" style="left:99px">
    <li><svg viewBox="0 0 14 14"><path d="M1 7l4 4 8-9" fill="none" stroke="#33b8a4" stroke-width="2.4"/></svg>Stunning Image Quality</li>
    <li><svg viewBox="0 0 14 14"><path d="M1 7l4 4 8-9" fill="none" stroke="#33b8a4" stroke-width="2.4"/></svg>Direct Social Sharing</li>
    <li><svg viewBox="0 0 14 14"><path d="M1 7l4 4 8-9" fill="none" stroke="#33b8a4" stroke-width="2.4"/></svg>Instant Prints</li>
  </ul>
  <div class="feature-divider"></div>
  <ul class="features" style="left:383px">
    <li><svg viewBox="0 0 14 14"><path d="M1 7l4 4 8-9" fill="none" stroke="#33b8a4" stroke-width="2.4"/></svg>Great Modern Design</li>
    <li><svg viewBox="0 0 14 14"><path d="M1 7l4 4 8-9" fill="none" stroke="#33b8a4" stroke-width="2.4"/></svg>Branding on Images</li>
    <li><svg viewBox="0 0 14 14"><path d="M1 7l4 4 8-9" fill="none" stroke="#33b8a4" stroke-width="2.4"/></svg>Custom Greenscreen Options</li>
  </ul>
  <a class="btn" style="left:99px;top:385px">Read More</a>
</section>
<div class="kiosk" role="img" aria-label="Freestanding white GIF booth kiosk with round camera lens"></div>

<div class="phones" role="img" aria-label="Two smartphones showing booth photos shared to social feeds"><div></div><div></div></div>
<h2 class="section-title abs" style="left:424px;top:1548px">Share Animated GIFs &nbsp;and Images Instantly On<br><span class="teal">Social Media</span></h2>
<p class="body-copy abs" style="left:424px;top:1636px;width:676px">Lorem Ipsum is simply dummy text of the printing and typesetting industry. Lorem Ipsum has been the industry's standard dummy text ever since the 1500s, when an unknown printer took a galley of type and scrambled it to make a type specimen book. It has survived not only five centuries, but also the leap into electronic typesettin gublishing software like Quirel PageSetter including Lorem Ipsum is simply dummy text of the printing.</p>
<a class="btn" style="left:424px;top:1790px">Read More</a>

<section class="galleries">
  <h2>Event <span class="teal">Galleries</span></h2>
  <span class="arrow" style="left:53px"></span>
  <span class="arrow" style="left:1118px"></span>
  <div class="thumb" style="left:99px;background:linear-gradient(135deg,#ddd,#888)" role="img" aria-label="Black and white booth photo of friends">
    <div class="thumb-caption">Lorem ipsum dolor sit <svg width="14" height="10" viewBox="0 0 14 10"><path d="M0 5h12M8 1l4 4-4 4" fill="none" stroke="#fff" stroke-width="2"/></svg></div>
  </div>
  <div class="thumb" style="left:303px;background:linear-gradient(135deg,#9a9a9f,#3c3c44)" role="img" aria-label="Guests posing with props on silver backdrop"></div>
  <div class="thumb" style="left:506px;background:linear-gradient(135deg,#7a5fa8,#3a2e6a)" role="img" aria-label="Group posing in front of purple backdrop"></div>
  <div class="thumb" style="left:710px;background:linear-gradient(135deg,#5a8acb,#7c5ab4)" role="img" aria-label="Friends with party props on blue backdrop"></div>
  <div class="thumb" style="left:912px;background:linear-gradient(135deg,#b03040,#4a1a20)" role="img" aria-label="Holiday party group in red hats"></div>
</section>

<h2 class="section-title blog-title">Latest <span class="teal">Blog</span></h2>
<article class="card" style="left:99px">
  <div class="photo" style="background:linear-gradient(135deg,#e7b7c6,#d56a8a 50%,#f4e0e6)" role="img" aria-label="Party guests with props at booth"><div class="date"><b>07</b><span>Apr<br>2015</span></div></div>
  <h3>Duis Autem Vel Eum Iriure Dolor In</h3>
  <div class="meta"><i></i>Ren Okaru &nbsp;/ &nbsp;<i></i>3 Comments</div>
  <p>Shoe street style leather tote oversized sweatshirt R.N.D. Varlo Seffino crop slipper denim shorts...[+]</p>
</article>
<article class="card" style="left:443px">
  <div class="photo" style="background:linear-gradient(135deg,#e8c65a,#c99a32 50%,#f0dca0)" role="img" aria-label="Friends posing on patterned yellow backdrop"><div class="date"><b>07</b><span>Apr<br>2015</span></div></div>
  <h3>Duis Autem Vel Eum Iriure Dolor In</h3>
  <div class="meta"><i></i>Ren Okaru &nbsp;/ &nbsp;<i></i>3 Comments</div>
  <p>Shoe street style leather tote oversized sweatshirt R.N.D. Varlo Seffino crop slipper denim shorts...[+]</p>
</article>
<article class="card" style="left:786px">
  <div class="photo" style="background:linear-gradient(135deg,#f2f2f2,#b9b6b2 50%,#5a504a)" role="img" aria-label="Three guests posing on white backdrop"><div class="date"><b>07</b><span>Apr<br>2015</span></div></div>
  <h3>Duis Autem Vel Eum Iriure Dolor In</h3>
  <div class="meta"><i></i>Ren Okaru &nbsp;/ &nbsp;<i></i>3 Comments</div>
  <p>Shoe street style leather tote oversized sweatshirt R.N.D. Varlo Seffino crop slipper denim shorts...[+]</p>
</article>

<footer class="site-footer">
  <div class="fcol" style="left:383px">
    <h4>Quick Links</h4>
    <ul class="links"><li>Home</li><li>About Us</li><li>GIF Photo Booth</li><li>Event Galleries</li><li>Blog</li><li>Contact Us</li></ul>
  </div>
  <div class="fcol" style="left:626px">
    <h4>Contact Us</h4>
    <div class="contact-row"><svg viewBox="0 0 16 16"><path d="M8 1a5 5 0 0 0-5 5c0 4 5 9 5 9s5-5 5-9a5 5 0 0 0-5-5z" fill="#ddd"/><circle cx="8" cy="6" r="2" fill="#2b2b2b"/></svg><span>Lorem Ipsum' Will Uncover Many<br>- 123456 Lorem Ipsum<br>Uncover Many - 123456</span></div>
    <div class="contact-row"><svg viewBox="0 0 16 16"><path d="M3 1l3 3-2 2c1 2 3 4 5 5l2-2 3 3-2 3C7 15 1 9 0 3z" fill="#ddd"/></svg><span>123-456-789</span></div>
    <div class="contact-row"><svg viewBox="0 0 16 16"><rect x="4" y="1" width="8" height="4" fill="#ddd"/><rect x="1" y="6" width="14" height="6" fill="#ddd"/><rect x="4" y="10" width="8" height="5" fill="#fff"/></svg><span>123-456-789</span></div>
    <div class="contact-row"><svg viewBox="0 0 16 16"><rect x="1" y="3" width="14" height="10" fill="none" stroke="#ddd" stroke-width="1.6"/><path d="M1 3l7 6 7-6" fill="none" stroke="#ddd" stroke-width="1.6"/></svg><span>info@zaberu.com</span></div>
  </div>
  <div class="fcol" style="left:932px">
    <h4>Follow Us</h4>
    <div class="socials"><span></span><span></span><span></span><span></span></div>
  </div>
</footer>
<div class="quote-box">
  <h4>Get Free Quote Now</h4>
  <div class="field">Your Name</div>
  <div class="field">Your Email</div>
  <div class="field">Phone...</div>
  <div class="submit">SUBMIT</div>
</div>
<div class="footer-brand">Zaberu</div>
<div class="copyright">Copyright© 2016 Zaberu. All rights reserved.</div>

</body>
</html>
```